B2B Software Company Needs 300x250 banner ad

I need a 300x250 static gif banner ad for a web site/online newsletter that we advertise on. We're a B2B software company, and the audience for this banner ad is medical device development team leads and managers. We would like to see designs that use blue (mainly), accent colors of orange, bright green, and purple are OK, too. This is a text heavy add but that can't be changed. I'm attaching our corporate logo, the copy file (Harbor Ledger.doc), latest version of our style guide, and an example of a previous ad we've done (which we don't necessarily need to/want to recreate). We want something that is pleasing to look at, easy to read, and gets someone to click through to the landing page.

Industry/Entity Type

Software

Requirements
Should not have
• Please do not re-lay out the 2013 outlook of Clinical Hardware Engineering banner. That was simply uploaded as an example. The docx Word document/copy should be used for a new banner ad.

```html
<!DOCTYPE html>
<html lang="en">
<head>
<meta charset="utf-8">
<title>Exclusive White Paper Banner</title>
<link rel="stylesheet" href="https://fonts.googleapis.com/css2?family=Arimo:wght@400;700&display=swap">
<style>
  :root {
    --stage: #ececec;
    --band-top: #0f4f8c;
    --band-bottom: #1a6cb3;
    --field-light: #2f9ae0;
    --field-deep: #0d5ea8;
    --ink-light: #ffffff;
    --ink-soft: #e6f4ff;
    --strip: #f7f7f7;
    --strip-edge: #d6d6d6;
    --logo-ink: #2a5d8f;
    --button-top: #8a5bd0;
    --button-bottom: #4e2a96;
    --button-ink: #1b1a4a;
  }
  * { box-sizing: border-box; margin: 0; padding: 0; }
  html, body {
    width: 1200px; height: 826px; overflow: hidden;
    background: var(--stage);
    font-family: "Arimo", Arial, sans-serif;
  }
  .banner {
    position: absolute; left: 150px; top: 38px;
    width: 900px; height: 750px; overflow: hidden;
    background: radial-gradient(ellipse at 30% 45%, var(--field-light) 0%, var(--field-deep) 75%);
    box-shadow: 0 6px 20px rgba(0,0,0,.25);
  }
  .banner__title-band {
    position: absolute; left: 0; top: 0; width: 100%; height: 114px;
    background: linear-gradient(var(--band-top), var(--band-bottom));
  }
  .banner__title {
    position: absolute; left: 33px; top: 22px;
    color: var(--ink-light); font-weight: 700; font-size: 64px; letter-spacing: -0.5px;
    text-shadow: 0 2px 3px rgba(0,0,0,.35);
  }
  .banner__subtitle {
    position: absolute; color: var(--ink-soft); font-weight: 400; font-size: 51px;
    letter-spacing: -0.3px; white-space: nowrap;
  }
  .banner__subtitle--first { left: 39px; top: 150px; }
  .banner__subtitle--second { left: 243px; top: 225px; }
  .banner__rule {
    position: absolute; height: 3px;
    background: linear-gradient(90deg, rgba(255,255,255,0), rgba(255,255,255,.9), rgba(255,255,255,0));
  }
  .banner__rule--first { left: 640px; top: 190px; width: 260px; }
  .banner__rule--second { left: 0; top: 268px; width: 240px; }
  .banner__body {
    position: absolute; left: 0; top: 322px; width: 100%;
    text-align: center; color: var(--ink-light); font-weight: 700;
    font-size: 46px; line-height: 63px; letter-spacing: -0.3px;
    text-shadow: 0 1px 2px rgba(0,0,0,.3);
  }
  .banner__footer {
    position: absolute; left: 0; top: 606px; width: 100%; height: 144px;
    background: linear-gradient(var(--strip), #e4e4e4);
    border-top: 2px solid var(--strip-edge);
  }
  .brand {
    position: absolute; left: 36px; top: 48px;
    display: flex; align-items: center; gap: 14px;
    color: var(--logo-ink); font-weight: 400; font-size: 40px;
  }
  .brand__dot { width: 26px; height: 26px; border-radius: 50%; background: var(--logo-ink); }
  .cta {
    position: absolute; left: 513px; top: 24px; width: 360px; height: 87px;
    border-radius: 44px;
    background: linear-gradient(var(--button-top), var(--button-bottom));
    box-shadow: inset 0 2px 0 rgba(255,255,255,.35), 0 3px 6px rgba(0,0,0,.3);
    color: var(--button-ink); font-weight: 700; font-size: 42px;
    display: flex; align-items: center; justify-content: center;
    text-decoration: none;
  }
</style>
</head>
<body>
  <div class="banner">
    <div class="banner__title-band"></div>
    <h1 class="banner__title">Exclusive White Paper</h1>
    <p class="banner__subtitle banner__subtitle--first">Exposing Risk In Product</p>
    <div class="banner__rule banner__rule--first"></div>
    <div class="banner__rule banner__rule--second"></div>
    <p class="banner__subtitle banner__subtitle--second">Development Lifecycles</p>
    <p class="banner__body">Reduce time spent managing risk<br>and support regulatory approvals<br>with traceability-based risk<br>management.</p>
    <div class="banner__footer">
      <div class="brand"><span class="brand__dot"></span><span class="brand__name">Larchfield Software</span></div>
      <a class="cta" href="#">Learn More</a>
    </div>
  </div>
</body>
</html>
```